Professional Services - letterhead / business cards

The company (veltaro holdings) will provide services to Investment Funds and large investors in Spain. I have recently chosen a logo that I am attaching.

I would like a simple stationary design that i could use as letter head, business cards and "with compliments" cards.

I am not quite sure which color I will mostly use for the logo, in the email signature I will probably lean towards the white background and grey letters. I am attaching my favourite options.

Target Market(s)

Large Multinationals, Investment funds and Law firms

Industry/Entity Type

Business

Requirements
Must have
• my details are:
Luis R. Andrade
Veltaro Holdings S.L.
Casa de Valdehondo
Calle del Olmo Tardío 42
28017 Madrid
T: +34 (91) 807-3356
M: +34 (655) 718-904
e-mail: landrade@veltaroholdings.example

```html
<!DOCTYPE html>
<html lang="en">
<head>
<meta charset="utf-8">
<title>Veltaro Holdings — Business Card</title>
<link rel="stylesheet" href="https://fonts.googleapis.com/css2?family=Questrial&family=Montserrat:wght@600&display=swap">
<style>
  :root {
    --page-bg: #e4e4e4;
    --card-bg: #3b3b3b;
    --card-shade: #333333;
    --text-light: #f2f2f2;
    --text-muted: #bdbdbd;
    --text-dim: #8c8c8c;
    --accent: #cfcfcf;
  }
  * { margin: 0; padding: 0; box-sizing: border-box; }
  html, body { width: 1200px; height: 900px; overflow: hidden; }
  body {
    background: var(--page-bg);
    font-family: "Questrial", sans-serif;
    display: flex;
    flex-direction: column;
    align-items: center;
    justify-content: center;
    gap: 40px;
  }
  .card {
    position: relative;
    width: 640px;
    height: 370px;
    background: linear-gradient(135deg, var(--card-bg), var(--card-shade));
    color: var(--text-light);
    box-shadow: 0 10px 24px rgba(0,0,0,0.25);
  }
  .wordmark {
    font-family: "Questrial", sans-serif;
    font-size: 36px;
    letter-spacing: 0.5px;
    color: var(--text-light);
    white-space: nowrap;
  }
  /* back side */
  .card-back .wordmark {
    position: absolute;
    left: 50%;
    top: 150px;
    transform: translateX(-50%);
  }
  .card-back .website {
    position: absolute;
    right: 70px;
    bottom: 50px;
    font-size: 12px;
    letter-spacing: 1px;
    color: var(--text-dim);
  }
  /* front side */
  .card-front .wordmark {
    position: absolute;
    left: 60px;
    top: 68px;
  }
  .edge-marker {
    position: absolute;
    left: 0;
    top: 270px;
    width: 12px;
    height: 20px;
  }
  .holder {
    position: absolute;
    left: 60px;
    top: 262px;
  }
  .holder-name {
    font-family: "Montserrat", sans-serif;
    font-weight: 600;
    font-size: 19px;
    color: var(--text-light);
    letter-spacing: 0.5px;
  }
  .holder-role {
    font-size: 18px;
    color: var(--text-dim);
    margin-top: 2px;
  }
  .contact {
    position: absolute;
    left: 360px;
    top: 150px;
    list-style: none;
    font-size: 14px;
    line-height: 20px;
    color: var(--text-muted);
  }
  .contact li {
    display: flex;
    align-items: flex-start;
    gap: 8px;
  }
  .contact svg {
    flex: 0 0 auto;
    width: 13px;
    height: 13px;
    margin-top: 3px;
    fill: var(--accent);
  }
</style>
</head>
<body>

  <section class="card card-back" aria-label="Business card, back">
    <div class="wordmark">veltaro holdings</div>
    <div class="website">www.veltaroholdings.example</div>
  </section>

  <section class="card card-front" aria-label="Business card, front">
    <div class="wordmark">veltaro holdings</div>

    <svg class="edge-marker" viewBox="0 0 12 20" aria-hidden="true">
      <polygon points="0,0 12,10 0,20" fill="#d6d6d6"/>
    </svg>

    <div class="holder">
      <div class="holder-name">Luis R. Andrade</div>
      <div class="holder-role">President</div>
    </div>

    <ul class="contact">
      <li>
        <svg viewBox="0 0 12 12" aria-hidden="true"><path d="M6 0a4 4 0 0 0-4 4c0 3 4 8 4 8s4-5 4-8a4 4 0 0 0-4-4zm0 5.6A1.6 1.6 0 1 1 6 2.4a1.6 1.6 0 0 1 0 3.2z"/></svg>
        <span>Calle del Olmo Tardío 42<br>28017 Madrid</span>
      </li>
      <li>
        <svg viewBox="0 0 12 12" aria-hidden="true"><path d="M1 4c0-1.5 2.2-2.5 5-2.5S11 2.5 11 4v1H8.5V3.8h-5V5H1z"/><rect x="2.5" y="6" width="7" height="5" rx="1"/></svg>
        <span>+34 (91) 807-3356</span>
      </li>
      <li>
        <svg viewBox="0 0 12 12" aria-hidden="true"><path d="M3 0h6a1 1 0 0 1 1 1v10a1 1 0 0 1-1 1H3a1 1 0 0 1-1-1V1a1 1 0 0 1 1-1zm0.8 1.5v5h4.4v-5z"/></svg>
        <span>+34 (655) 718-904</span>
      </li>
      <li>
        <svg viewBox="0 0 12 12" aria-hidden="true"><path d="M0 2h12v8H0zm1.2 1 4.8 3.6L10.8 3v-.2H1.2z"/></svg>
        <span>landrade@veltaroholdings.example</span>
      </li>
    </ul>
  </section>

</body>
</html>
```